Stylish new business card needed!

Hello everyone! I am in need of a new business card design for an alarm company here in Hurricane WV. I have all fonts, color codes and logos provided for you use! We are a young company and like the style of a clean sleek looking business card. Would like it double sided, one side holding the logo and the other with your design!
Target Market(s)
The people that are looking for the newest tech for home automation and security
Industry/Entity Type
Alarm services; Home automation
Contact Information for Business Card
Name of person; position (Sales; Installer); Phone Number (555.419.7362); Employee cell Number; Website (www.GuardedByVelm.example); Employee Email; Double sided
Look and feel
Each slider illustrates characteristics of the customer's brand and the style your logo design should communicate.

```html
<!DOCTYPE html>
<html lang="en">
<head>
<meta charset="utf-8">
<title>Velm Business Card – Front and Back</title>
<link rel="stylesheet" href="https://fonts.googleapis.com/css2?family=Archivo+Black&family=Poppins:wght@300;400;500;600&display=swap">
<style>
  :root {
    --stage: #ebebeb;
    --card-dark: #231f20;
    --card-light: #ffffff;
    --accent: #e6925c;
    --logo-grey: #9a9a9a;
    --ink: #1e1e1e;
    --ink-soft: #333333;
    --white: #ffffff;
  }
  * { box-sizing: border-box; margin: 0; padding: 0; }
  html, body {
    width: 1200px;
    height: 800px;
    overflow: hidden;
    background: var(--stage);
    font-family: "Poppins", sans-serif;
  }
  .stage {
    position: relative;
    width: 1200px;
    height: 800px;
  }
  .card {
    position: absolute;
    top: 257px;
    width: 500px;
    height: 286px;
    overflow: hidden;
  }

  /* Brand side */
  .card--brand {
    left: 70px;
    background: var(--card-dark);
  }
  .brand-tagline {
    position: absolute;
    left: 104px;
    top: 58px;
    font-family: "Archivo Black", sans-serif;
    font-size: 30px;
    letter-spacing: 3px;
    color: var(--accent);
  }
  .brand-lockup {
    position: absolute;
    left: 90px;
    top: 96px;
    display: flex;
    align-items: center;
    gap: 18px;
  }
  .brand-mark {
    width: 40px;
    height: 40px;
    border-radius: 50%;
    background: var(--accent);
  }
  .brand-name {
    font-family: "Poppins", sans-serif;
    font-weight: 500;
    font-size: 112px;
    line-height: 1;
    letter-spacing: 4px;
    color: var(--white);
  }
  .brand-service {
    position: absolute;
    left: 104px;
    bottom: 30px;
    font-family: "Archivo Black", sans-serif;
    font-size: 13px;
    letter-spacing: 2px;
    color: var(--accent);
  }

  /* Contact side */
  .card--contact {
    left: 630px;
    background: var(--card-light);
  }
  .contact-logo {
    position: absolute;
    left: 42px;
    top: 34px;
    display: flex;
    align-items: center;
    gap: 10px;
  }
  .contact-logo__mark {
    width: 20px;
    height: 20px;
    border-radius: 50%;
    background: var(--accent);
  }
  .contact-logo__name {
    font-weight: 400;
    font-size: 48px;
    line-height: 1;
    letter-spacing: 2px;
    color: var(--logo-grey);
  }
  .person {
    position: absolute;
    left: 42px;
    bottom: 56px;
  }
  .person__name {
    font-weight: 600;
    font-size: 18px;
    color: var(--ink);
  }
  .person__role {
    font-weight: 300;
    font-size: 12px;
    color: var(--ink-soft);
    margin-top: 2px;
  }
  .contact-list {
    position: absolute;
    right: 36px;
    bottom: 52px;
    list-style: none;
    text-align: right;
    font-weight: 300;
    font-size: 12.5px;
    line-height: 1.6;
    color: var(--ink-soft);
  }
</style>
</head>
<body>
  <main class="stage">
    <section class="card card--brand" aria-label="Card back with brand">
      <p class="brand-tagline">GUARDED BY</p>
      <div class="brand-lockup">
        <span class="brand-mark" aria-hidden="true"></span>
        <span class="brand-name">VELM</span>
      </div>
      <p class="brand-service">AUTOMATION &amp; SECURITY</p>
    </section>

    <section class="card card--contact" aria-label="Card front with contact details">
      <div class="contact-logo">
        <span class="contact-logo__mark" aria-hidden="true"></span>
        <span class="contact-logo__name">VELM</span>
      </div>
      <div class="person">
        <p class="person__name">Name Surname</p>
        <p class="person__role">POSITION</p>
      </div>
      <ul class="contact-list">
        <li class="contact-list__office">555.419.7362</li>
        <li class="contact-list__cell">555.419.7362</li>
        <li class="contact-list__email">name@guardedbyvelm.example</li>
        <li class="contact-list__web">www.guardedbyvelm.example</li>
      </ul>
    </section>
  </main>
</body>
</html>
```